New business card with our logo

we finalized our logo with the help of pixel harbor - now we need a business card using that logo. we are a metal service center providing raw steel and metal products for fabricating, contractors, artists, etc. we have the wording for the back of the card figured out (attached, no deviations from text please), just need help putting it all together.
would like the look of steel somehow incorporated in the design ... would like the black part of the logo to be steel or silver color (the S & BRANLEY)
Other font styles liked:
- calibri, arial, similar to those, modern looking
Colors
Designer to choose colors to be used in the design.
Requirements
Must have
- Back of card must haves are attached (no deviations from wording please).
- FRONT of card:
- logo
- address
- name
- office tel
- cell
- fax
- website
- address
Nice to have
- incorporate the look of steel or element of steel somehow
- names of the staff on front not in all caps, i.e. Rosvita not ROSVITA
- this industry is more industrial, not coffee or flower shop so design should be aligned with that
- design should be classic and tasteful

```html
<!DOCTYPE html>
<html lang="en">
<head>
<meta charset="utf-8">
<title>Branley Steel – Business Card</title>
<link href="https://fonts.googleapis.com/css2?family=Lato:wght@300;400;700;900&display=swap" rel="stylesheet">
<style>
  :root{
    --bg:#1b1d1f;
    --card:#1e2024;
    --card-edge:#26292e;
    --silver:#d9dde2;
    --silver-dark:#8f959c;
    --text:#e6e8eb;
    --muted:#a7adb4;
    --blue:#1a73c4;
    --blue-bright:#2b8ee0;
    --blue-deep:#0b4f96;
  }
  *{box-sizing:border-box;margin:0;padding:0}
  html,body{width:1200px;height:1200px;overflow:hidden;background:var(--bg);font-family:'Lato',Arial,sans-serif;color:var(--text)}
  .canvas{position:relative;width:1200px;height:1200px}
  .card{position:absolute;left:120px;width:960px;height:548px;background:linear-gradient(160deg,var(--card-edge),var(--card) 55%,#191b1e);overflow:hidden;box-shadow:0 10px 30px rgba(0,0,0,.45)}
  .card--back{top:32px}
  .card--front{top:620px}

  /* back */
  .faint-circle{position:absolute;right:70px;top:40px;width:290px;height:290px;border-radius:50%;border:22px solid rgba(255,255,255,.035)}
  .headline{position:absolute;left:48px;top:78px;font-weight:900;font-size:44px;letter-spacing:1px;background:linear-gradient(180deg,#ffffff,var(--silver) 45%,var(--silver-dark));-webkit-background-clip:text;background-clip:text;color:transparent}
  .services{position:absolute;left:96px;top:140px;font-size:22px;letter-spacing:.5px;color:var(--text)}
  .services .dot{display:inline-block;width:8px;height:8px;border-radius:50%;background:var(--blue-bright);margin:0 8px 4px}
  .services-rule{position:absolute;left:130px;top:178px;width:360px;height:2px;background:linear-gradient(90deg,transparent,var(--blue-bright),transparent)}
  .checklist{position:absolute;top:240px;list-style:none;font-size:22px;line-height:31px}
  .checklist--left{left:66px}
  .checklist--right{left:440px;top:226px}
  .checklist li{display:flex;align-items:center;gap:8px}
  .checklist svg{width:18px;height:18px}
  .brand{position:absolute;display:flex;align-items:center;gap:22px}
  .brand--back{left:76px;top:372px}
  .brand__circle{border-radius:50%;border:6px solid var(--blue);flex:none}
  .brand--back .brand__circle{width:120px;height:120px}
  .brand__name{font-weight:900;color:var(--silver);letter-spacing:1px;white-space:nowrap}
  .brand--back .brand__name{font-size:52px}
  .tagline{position:absolute;right:64px;top:476px;font-size:28px;letter-spacing:3px;color:var(--blue-bright);white-space:nowrap}

  /* front */
  .brand--front{left:56px;top:80px;width:420px;flex-direction:column;gap:24px}
  .brand--front .brand__circle{width:190px;height:190px;border-width:8px}
  .brand--front .brand__name{font-size:50px}
  .divider{position:absolute;left:520px;top:70px;width:2px;height:290px;background:linear-gradient(180deg,transparent,var(--blue-bright),transparent)}
  .person{position:absolute;left:572px;top:76px}
  .person__name{font-size:40px;font-weight:400;color:var(--text)}
  .person__role{font-size:22px;font-weight:300;color:var(--muted);margin-top:2px}
  .contacts{position:absolute;left:572px;top:196px;list-style:none;font-size:23px;line-height:32px}
  .contacts li{display:flex;align-items:center;gap:16px}
  .contacts li.address{align-items:flex-start;line-height:26px;margin-bottom:16px;font-size:20px}
  .contacts svg{width:20px;height:20px;flex:none;margin-top:3px}
  .band-line{position:absolute;left:0;right:0;bottom:104px;height:1px;background:var(--blue)}
  .band{position:absolute;left:0;right:0;bottom:0;height:92px;background:linear-gradient(90deg,var(--blue-deep),var(--blue) 60%,var(--blue-bright))}
</style>
</head>
<body>
<div class="canvas">

  <section class="card card--back">
    <div class="faint-circle"></div>
    <h1 class="headline">METAL SERVICES CENTER</h1>
    <p class="services">CUT<span class="dot"></span>SHEAR<span class="dot"></span>PUNCH<span class="dot"></span>LIGHT FAB</p>
    <div class="services-rule"></div>

    <ul class="checklist checklist--left">
      <li><svg viewBox="0 0 20 20"><path d="M2 11l5 5L18 3" fill="none" stroke="#2b8ee0" stroke-width="3"/></svg>Structural Steel</li>
      <li><svg viewBox="0 0 20 20"><path d="M2 11l5 5L18 3" fill="none" stroke="#2b8ee0" stroke-width="3"/></svg>Stainless &amp; Aluminum</li>
      <li><svg viewBox="0 0 20 20"><path d="M2 11l5 5L18 3" fill="none" stroke="#2b8ee0" stroke-width="3"/></svg>Building Components</li>
    </ul>
    <ul class="checklist checklist--right">
      <li><svg viewBox="0 0 20 20"><path d="M2 11l5 5L18 3" fill="none" stroke="#2b8ee0" stroke-width="3"/></svg>Rebar</li>
      <li><svg viewBox="0 0 20 20"><path d="M2 11l5 5L18 3" fill="none" stroke="#2b8ee0" stroke-width="3"/></svg>Decking</li>
      <li><svg viewBox="0 0 20 20"><path d="M2 11l5 5L18 3" fill="none" stroke="#2b8ee0" stroke-width="3"/></svg>... And more!</li>
    </ul>

    <div class="brand brand--back">
      <span class="brand__circle"></span>
      <span class="brand__name">BRANLEY STEEL</span>
    </div>
    <p class="tagline">Pick-up or Delivered!</p>
  </section>

  <section class="card card--front">
    <div class="brand brand--front">
      <span class="brand__circle"></span>
      <span class="brand__name">BRANLEY STEEL</span>
    </div>
    <div class="divider"></div>

    <div class="person">
      <p class="person__name">Daniel Harwick</p>
      <p class="person__role">Director</p>
    </div>

    <ul class="contacts">
      <li class="address"><svg viewBox="0 0 20 20"><path d="M10 1a6 6 0 0 0-6 6c0 5 6 12 6 12s6-7 6-12a6 6 0 0 0-6-6z" fill="#2b8ee0"/><circle cx="10" cy="7" r="2.2" fill="#1e2024"/></svg><span>Street adress, lorem ipsum<br>Your city, 1568</span></li>
      <li><svg viewBox="0 0 20 20"><path d="M3 8c0-3 14-3 14 0v2h-4V8H7v2H3z M5 11h10l1 6H4z" fill="#2b8ee0"/></svg>123 456 7890</li>
      <li><svg viewBox="0 0 20 20"><rect x="6" y="2" width="8" height="16" rx="1.5" fill="#2b8ee0"/><rect x="7.5" y="4" width="5" height="9" fill="#1e2024"/></svg>001 235 4589</li>
      <li><svg viewBox="0 0 20 20"><rect x="5" y="2" width="10" height="6" fill="none" stroke="#2b8ee0" stroke-width="1.6"/><rect x="2" y="8" width="16" height="9" rx="1" fill="#2b8ee0"/></svg>123 456 7898</li>
      <li><svg viewBox="0 0 20 20"><g fill="none" stroke="#2b8ee0" stroke-width="1.5"><circle cx="10" cy="10" r="8"/><ellipse cx="10" cy="10" rx="3.5" ry="8"/><path d="M2 10h16M3.5 6h13M3.5 14h13"/></g></svg>yourwebsitename.com</li>
      <li><svg viewBox="0 0 20 20"><g fill="none" stroke="#2b8ee0" stroke-width="1.5"><rect x="2" y="4" width="16" height="12"/><path d="M2 4l8 7 8-7"/></g></svg>yourname@emal.com</li>
    </ul>

    <div class="band-line"></div>
    <div class="band"></div>
  </section>

</div>
</body>
</html>
```